Banner for County Fair

Need a banner with our logo primarily, but some other color/background work. Also include city name West Point, NE. Tagline that could be used is Fiber Optic Fast! Also visit www.tollbarnetlink.com to get a feel for the company.

```html
<!DOCTYPE html>
<html lang="en">
<head>
<meta charset="utf-8">
<title>West Point Nebraska – Fiber Optic Fast</title>
<link href="https://fonts.googleapis.com/css2?family=Oswald:wght@400;500;700&display=swap" rel="stylesheet">
<style>
  :root {
    --sky-top: #c9d3de;
    --sky-mid: #8e9db1;
    --city-dark: #3d4b5e;
    --city-glow: #d79a55;
    --night: #1b2433;
    --night-deep: #0f151f;
    --white: #ffffff;
    --brand-blue: #1f3f8f;
    --bar: rgba(20, 24, 32, 0.82);
  }
  html, body {
    margin: 0;
    padding: 0;
    overflow: hidden;
    background: #ffffff;
  }
  .banner {
    position: relative;
    width: 1200px;
    height: 379px;
    overflow: hidden;
    font-family: "Oswald", "Arial Narrow", sans-serif;
    color: var(--white);
  }
  .cityscape {
    position: absolute;
    inset: 0 300px 0 0;
    background:
      radial-gradient(ellipse 380px 140px at 300px 330px, rgba(215,154,85,0.55), transparent 70%),
      linear-gradient(180deg, var(--sky-top) 0%, var(--sky-mid) 32%, var(--city-dark) 62%, #2a3442 100%);
  }
  .worker-photo {
    position: absolute;
    top: 0;
    right: 0;
    width: 560px;
    height: 100%;
    background:
      linear-gradient(90deg, rgba(61,75,94,0) 0%, rgba(27,36,51,0.85) 30%, var(--night) 55%, var(--night-deep) 100%);
  }
  .brand {
    position: absolute;
    left: 32px;
    top: 34px;
    display: flex;
    align-items: center;
    gap: 10px;
  }
  .brand-dot {
    width: 26px;
    height: 26px;
    border-radius: 50%;
    background: var(--brand-blue);
  }
  .brand-name {
    font-size: 38px;
    font-weight: 500;
    color: var(--brand-blue);
    line-height: 1;
  }
  .location {
    position: absolute;
    left: 445px;
    top: 104px;
    width: 308px;
    text-align: right;
  }
  .location-city {
    display: block;
    font-size: 64px;
    font-weight: 500;
    line-height: 1;
    letter-spacing: -0.5px;
    text-shadow: 0 2px 6px rgba(0,0,0,0.35);
  }
  .location-state {
    display: block;
    font-size: 19px;
    font-weight: 500;
    line-height: 1.2;
    margin-top: 2px;
    letter-spacing: 0.5px;
  }
  .tagline {
    position: absolute;
    left: 108px;
    top: 186px;
    width: 980px;
    margin: 0;
    font-size: 138px;
    font-weight: 700;
    line-height: 1;
    letter-spacing: 1px;
    white-space: nowrap;
    color: rgba(255,255,255,0.94);
    text-shadow: 0 3px 10px rgba(0,0,0,0.3);
  }
  .support-bar {
    position: absolute;
    left: 0;
    bottom: 0;
    width: 100%;
    height: 40px;
    background: var(--bar);
    display: flex;
    align-items: center;
    padding-left: 368px;
    box-sizing: border-box;
    font-size: 19px;
    font-weight: 500;
    letter-spacing: 0.3px;
  }
  .support-icon {
    width: 26px;
    height: 26px;
    margin-right: 12px;
  }
  .support-divider {
    margin: 0 16px;
    opacity: 0.9;
  }
</style>
</head>
<body>
  <div class="banner">
    <div class="cityscape" role="img" aria-label="Evening city skyline with high-rise towers, cranes and a glowing highway"></div>
    <div class="worker-photo" role="img" aria-label="Man working on a laptop in a dim blue room"></div>

    <div class="brand">
      <span class="brand-dot"></span>
      <span class="brand-name">tollbar</span>
    </div>

    <div class="location">
      <span class="location-city">WEST POINT</span>
      <span class="location-state">NEBRASKA</span>
    </div>

    <h1 class="tagline">FIBER OPTIC FAST!</h1>

    <div class="support-bar">
      <svg class="support-icon" viewBox="0 0 26 26" aria-hidden="true">
        <circle cx="13" cy="9" r="5.5" fill="#ffffff"/>
        <path d="M4 25c0-6 4-9.5 9-9.5s9 3.5 9 9.5z" fill="#ffffff"/>
        <path d="M6.5 10a6.5 6.5 0 0 1 13 0" fill="none" stroke="#ffffff" stroke-width="1.6"/>
        <circle cx="19" cy="20" r="4" fill="#c0392b"/>
      </svg>
      <span class="support-label">TECH SUPPORT:&nbsp; 888-555-0142</span>
      <span class="support-divider">|</span>
      <span class="support-number">402-555-0186</span>
    </div>
  </div>
</body>
</html>
```